Push notification screens at app start up

We have an existing news publication app platform and are adding categories to push notifications.

We need two screens designed (each for Novaro, Tavlet and Morvelin for a total of 6d) that show when the app is first launched.

The workflow of our app:
0. app launch screen while webservices run (no work needed)
1. information screen to the user promoting the benefits of push notification with "Next" button. (see concept attached)
2. Push categories selection screen. This will have list of category types, with on/off switch.

"Select the categories that you wish to receive occasional notices:
Breaking News (on/off switch)
Local News (on/off switch)
Sports (on/off switch)
Local Events (on/off switch)
Weather Alerts (on/off switch)
Local Deals (on/off switch)"

"Enable these categories on the next screen."
"Next" button

Background:
When I was looking around at app designs, I came across this one (http://www.pixelvane.net/design/7148305) and I really liked it. We obviously have different features on our screen, but I’d like to have this same feel. The colors used in this design are perfect.

UPDATE: I do not mean to limit your design to match the layout as the one mentioned above. Please use your creativity for the layout.

Our standard font in Helvetica Neue.

Notes:
- our app is developed for all phone devices from Novaro 4 to Novaro 6, so designs should be thoughtful of vertical scrolling if needed.
- our app is developed for Tavlets, so we'll need designs completed as well. (We can finalize Novaro design first, then translate the design to Tavlet.)
- our app is developed for Morvelin phones (not tablets), so we'll need designs completed as well. (We can finalize Kvo design first, then translater to Morvelin UI design guidelines).

We hope to establish a good on-going relationship with the designer for as-needed work in the future.

Industry/Entity Type

News

Font styles to use
Other font styles liked:
• Helvetica Neue

Requirements
Must have
• Clean designs. No clutter.
Nice to have
• We would likely go with the standard on/off switches for both Kvo and Morvelin, but are open to small custom variations.

```html
<!DOCTYPE html>
<html lang="en">
<head>
<meta charset="UTF-8">
<title>Notifications</title>
<link href="https://fonts.googleapis.com/css2?family=Inter:wght@400;500;600;700&display=swap" rel="stylesheet">
<style>
  :root {
    --brand-blue: #2f7ff2;
    --switch-blue: #2a72e6;
    --page-grey: #e4e4e4;
    --row-white: #ffffff;
    --divider: #dcdcdc;
    --label-grey: #555a60;
    --body-grey: #3f3f3f;
    --switch-border: #d8d8d8;
  }
  * { box-sizing: border-box; margin: 0; padding: 0; }
  html, body { width: 675px; height: 1200px; overflow: hidden; }
  body {
    font-family: "Inter", "Helvetica Neue", Arial, sans-serif;
    background: var(--page-grey);
    position: relative;
  }
  .app-header {
    background: var(--brand-blue);
    height: 135px;
    color: #fff;
    position: relative;
  }
  .status-bar {
    height: 45px;
    display: flex;
    align-items: center;
    justify-content: space-between;
    padding: 0 14px;
    font-size: 18px;
    font-weight: 500;
  }
  .status-left, .status-right { display: flex; align-items: center; gap: 8px; width: 220px; }
  .status-right { justify-content: flex-end; }
  .status-time { font-weight: 600; }
  .signal { display: flex; gap: 3px; }
  .signal span { width: 9px; height: 9px; border-radius: 50%; border: 1.5px solid #fff; }
  .signal span.full { background: #fff; }
  .nav-bar {
    height: 90px;
    display: flex;
    align-items: center;
    justify-content: center;
    position: relative;
  }
  .nav-title { font-size: 34px; font-weight: 600; letter-spacing: 0.2px; }
  .back-button { position: absolute; left: 26px; top: 28px; }
  .category-list {
    list-style: none;
    margin-top: 50px;
    background: var(--row-white);
    border-top: 1px solid var(--divider);
    border-bottom: 1px solid var(--divider);
  }
  .category-row {
    height: 99px;
    display: flex;
    align-items: center;
    padding: 0 14px 0 22px;
    border-bottom: 1px solid var(--divider);
  }
  .category-row:last-child { border-bottom: none; }
  .category-icon { width: 48px; height: 48px; flex: none; }
  .category-name {
    margin-left: 34px;
    font-size: 27px;
    font-weight: 700;
    color: var(--label-grey);
    flex: 1;
  }
  .switch {
    width: 92px; height: 56px;
    border-radius: 28px;
    border: 2px solid var(--switch-border);
    background: #fff;
    position: relative;
  }
  .switch::after {
    content: "";
    position: absolute;
    top: 1px; left: 1px;
    width: 50px; height: 50px;
    border-radius: 50%;
    background: #fff;
    box-shadow: 0 2px 5px rgba(0,0,0,0.25);
  }
  .switch.is-on { background: var(--switch-blue); border-color: var(--switch-blue); }
  .switch.is-on::after { left: auto; right: 1px; }
  .footnote {
    width: 530px;
    margin: 28px auto 0;
    text-align: center;
    font-size: 17.5px;
    line-height: 25px;
    color: var(--body-grey);
  }
  .next-button {
    display: block;
    width: 575px;
    height: 80px;
    margin: 40px auto 0;
    border: none;
    border-radius: 10px;
    background: var(--brand-blue);
    color: #fff;
    font-family: inherit;
    font-size: 28px;
    font-weight: 600;
  }
</style>
</head>
<body>
  <header class="app-header">
    <div class="status-bar">
      <div class="status-left">
        <div class="signal"><span class="full"></span><span class="full"></span><span class="full"></span><span></span><span></span></div>
        <span>KESTREL</span>
        <svg width="22" height="16" viewBox="0 0 22 16"><path d="M1 5a15 15 0 0 1 20 0M4.5 8.5a10 10 0 0 1 13 0M8 12a5 5 0 0 1 6 0" fill="none" stroke="#fff" stroke-width="2.2" stroke-linecap="round"/><circle cx="11" cy="14.5" r="1.5" fill="#fff"/></svg>
      </div>
      <span class="status-time">4:21 PM</span>
      <div class="status-right">
        <svg width="12" height="18" viewBox="0 0 12 18"><path d="M1 5l9 8-4.5 4V1L10 5l-9 8" fill="none" stroke="#fff" stroke-width="1.6" stroke-linejoin="round"/></svg>
        <span>100%</span>
        <svg width="44" height="20" viewBox="0 0 44 20"><rect x="1" y="2" width="38" height="16" rx="3" fill="none" stroke="#fff" stroke-width="1.6"/><rect x="3.5" y="4.5" width="33" height="11" rx="1.5" fill="#fff"/><rect x="40.5" y="7" width="2.5" height="6" rx="1" fill="#fff"/></svg>
      </div>
    </div>
    <nav class="nav-bar">
      <svg class="back-button" width="24" height="36" viewBox="0 0 24 36"><path d="M20 3L5 18l15 15" fill="none" stroke="#fff" stroke-width="4.5" stroke-linecap="round" stroke-linejoin="round"/></svg>
      <h1 class="nav-title">Notifications</h1>
    </nav>
  </header>

  <main>
    <ul class="category-list">
      <li class="category-row">
        <svg class="category-icon" viewBox="0 0 48 48" fill="none" stroke="#2f7ff2" stroke-width="2.4">
          <rect x="9" y="5" width="30" height="38" rx="1"/><rect x="14" y="11" width="9" height="9"/><path d="M27 12h7M27 17h7M14 25h20M14 30h20M14 35h14"/><path d="M9 43H5V14h4"/>
        </svg>
        <span class="category-name">Breaking News</span>
        <span class="switch"></span>
      </li>
      <li class="category-row">
        <svg class="category-icon" viewBox="0 0 48 48" fill="none" stroke="#2f7ff2" stroke-width="2.4">
          <rect x="6" y="8" width="36" height="32" rx="1"/><rect x="11" y="14" width="12" height="10"/><path d="M27 15h10M27 20h10M11 29h26M11 34h26"/>
        </svg>
        <span class="category-name">Local News</span>
        <span class="switch is-on"></span>
      </li>
      <li class="category-row">
        <svg class="category-icon" viewBox="0 0 48 48" fill="none" stroke="#2f7ff2" stroke-width="2.4">
          <circle cx="24" cy="24" r="17"/><path d="M10 14c6 5 6 15 0 20M38 14c-6 5-6 15 0 20"/>
        </svg>
        <span class="category-name">Sports</span>
        <span class="switch"></span>
      </li>
      <li class="category-row">
        <svg class="category-icon" viewBox="0 0 48 48" fill="none" stroke="#2f7ff2" stroke-width="2.4">
          <rect x="5" y="9" width="38" height="33" rx="2"/><path d="M5 17h38M14 5v8M34 5v8"/><rect x="11" y="22" width="6" height="5"/><rect x="21" y="22" width="6" height="5"/><rect x="31" y="22" width="6" height="5"/><rect x="11" y="32" width="6" height="5"/><rect x="21" y="32" width="6" height="5"/><rect x="31" y="32" width="6" height="5"/>
        </svg>
        <span class="category-name">Local Events</span>
        <span class="switch"></span>
      </li>
      <li class="category-row">
        <svg class="category-icon" viewBox="0 0 48 48" fill="none" stroke="#2f7ff2" stroke-width="2.4" stroke-linecap="round">
          <circle cx="28" cy="17" r="6"/><path d="M28 5v3M39 17h3M36 9l2-2M20 9l-2-2M36 25l2 2"/>
          <path d="M10 39h24a6 6 0 0 0 0-12 9 9 0 0 0-17-2 7 7 0 0 0-7 14z" fill="#2f7ff2"/>
        </svg>
        <span class="category-name">Weather Alerts</span>
        <span class="switch"></span>
      </li>
      <li class="category-row">
        <svg class="category-icon" viewBox="0 0 48 48">
          <path d="M6 8v15l20 20 17-17L23 6H8a2 2 0 0 0-2 2z" fill="#2f7ff2"/><circle cx="14" cy="14" r="3.5" fill="#fff"/>
        </svg>
        <span class="category-name">Local Deals</span>
        <span class="switch"></span>
      </li>
    </ul>

    <p class="footnote">Select the categories that you wish to receive occasional notices. Enable these categories on the next screen.</p>
    <button class="next-button" type="button">Next</button>
  </main>
</body>
</html>
```